Web-Design  für naturwissenschaflich-philosophische Institution
Zielgruppe
Es handelt sich um eine naturwissenschaflich-philosophische Institution. Besucher sind neben Natur- und Geisteswissenschaftlern auch interessierte Laien.
Kernthema der Seite ist alles rund um das Thema Zahlen, allerdings unter einem naturwissenschaftlich, philosophischen Aspekt. Nach einer grundsätzlichen Erklärung (Leitartikel 'Als Flüsse singen') baut die Seite sich auf aus zahreichen Beispielen/Beiträgen aus den unterschiedlichsten Fachbereichen, die scheinbar keinerlei Bezug zueinander haben, wie Mathematik, Geometrie einerseits und der großen Literatur einschließlich historischer und religiöser Schriften andererseits. Immer aber gibt es einen Bezug zu fraktal wachsenden Dreiecken.
Die Artikel sind meist populärwissenschaftlich formuliert. Es handelt sich nicht um esoterische Inhalte, auch wenn der Domainname www.kelmbrauth.de das evtl. vermuten ließe. Keine Berührung zu Spiritualität. Die Institution ist im Aufbau und hat durchaus den Anspruch, diese klassischen Themen modern aufzugreifen. Sie ist nicht verstaubt.
Aufgabenstellung
Geordneter, klarer, transparenter Aufbau. Übersichtlich und strukturiert, wie zB www.qrl.de Es sollten geometrische Proportionen eingehalten werden (wie Symmetrie, goldener Schnitt). Nicht zu viele verschiedene Stilelemente. Die Seite sollte einladend sein, ggf. ansprechendes Bild auf Startseite (mit Bezug zu Zahlen, Geoemetrie).
Die Startseite braucht nun im Header kein Logo mehr zu haben. Der Seitentitel sollte sein 'Das Echo der Wolken'. Siehe Anhang 'Header Beispiel'
Als Menüpunkte benötigen wir neben Home, nur 'Beiträge', 'Buch', 'Kontakt' oder einfach nur die bekannten drei Striche. Der Link zum Impressum genügt im Footer. Rechts oben benötigt man ein Suchfeld.
Besonderheit: Man benötigt eine Art zweiten Header, der aus einer Zahlenreihe besteht. Die einzelnen Zahlen müssen später verlinkt sein auf Unterseiten. Siehe Muster im Anhang. Der User muss sie als Link erkennen können (evtl. Programmierthema: zB Hervorheben beim drüberhoovern). Die Zahlen müssen erweiterbar sein, ggf. über Pfeil klicken, siehe
Es gibt einen zentralen Startartikel. Auf diesen muss man leicht kommen. Im Muster heißt er 'Als die Flüsse singen'.
Das Bild hier ist sehr wichtig. Es sollte bestehn aus vielen interessanten Zahlen, wie in 'Zahlenwolke' angegeben. Und möglichst auch den Dreiecken wie in 'Logo1'.
Weiter unten auf der Startseite sollte es dann weitere Elemente geben, einmal wo man zu bestimmten Unterkategorien kommt, im Muster sind das 'Bibel und Zahlen' 'Naturwissenschaft' etc. und dann evtl weiter unten noch ein Stilelemente, in welchem man die neuesten Artikel verlinken kann.

```html
<!DOCTYPE html>
<html lang="de">
<head>
<meta charset="utf-8">
<title>Das Echo der Wolken</title>
<link rel="stylesheet" href="https://fonts.googleapis.com/css2?family=Poppins:wght@400;500;600;700;800&display=swap">
<style>
  :root {
    --page-bg: #f2f2f2;
    --white: #ffffff;
    --band: #ececec;
    --blue: #1b7fe6;
    --blue-title: #1a80e0;
    --ink: #2a3444;
    --ink-soft: #4a5260;
    --hero-a: #3a7ccf;
    --hero-b: #4aa2e6;
    --card-bg: #f2f2f2;
    --line: #c9ccd2;
  }
  * { box-sizing: border-box; margin: 0; padding: 0; }
  html, body { width: 1200px; height: 2447px; overflow: hidden; }
  body {
    background: var(--page-bg);
    font-family: "Poppins", sans-serif;
    color: var(--ink);
    position: relative;
  }
  .site {
    position: absolute;
    left: 0; top: 600px;
    width: 1200px; height: 1248px;
    background: var(--white);
  }
  .site-header {
    position: absolute; left: 0; top: 0; width: 1200px; height: 63px;
    background: var(--white);
  }
  .site-title {
    position: absolute; left: 176px; top: 17px;
    font-size: 21px; font-weight: 400; color: var(--blue-title);
    letter-spacing: 0.2px;
  }
  .main-nav {
    position: absolute; left: 530px; top: 24px;
    display: flex; align-items: center;
    font-size: 11px; font-weight: 600; color: var(--ink);
  }
  .main-nav a { color: inherit; text-decoration: none; padding: 0 12px; border-left: 1px solid var(--line); line-height: 12px; }
  .main-nav a:first-child { border-left: none; }
  .search {
    position: absolute; left: 900px; top: 19px; width: 124px; height: 24px;
    border: 1px solid #8a8f98; border-radius: 3px; background: var(--white);
    font-size: 10px; color: #c4c7cc; padding: 5px 6px;
  }
  .search svg { position: absolute; right: 6px; top: 5px; }
  .number-bar {
    position: absolute; left: 0; top: 63px; width: 1200px; height: 37px;
    background: var(--band);
  }
  .number-bar .label {
    position: absolute; left: 622px; top: 11px;
    font-size: 11.5px; font-weight: 500; color: var(--ink);
  }
  .number-bar .arrow { position: absolute; top: 14px; }
  .number-list { position: absolute; left: 789px; top: 10px; display: flex; gap: 7px; }
  .number-list a {
    width: 18px; height: 18px; border-radius: 3px;
    background: var(--ink); color: var(--white);
    font-size: 13px; font-weight: 600; line-height: 18px; text-align: center;
    text-decoration: none;
  }
  .number-list a.is-active { background: var(--blue); }
  .hero {
    position: absolute; left: 0; top: 100px; width: 1200px; height: 523px;
  }
  .hero-art {
    position: absolute; inset: 0;
    background: linear-gradient(120deg, var(--hero-a) 0%, #3d86d8 45%, var(--hero-b) 100%);
  }
  .hero-title {
    position: absolute; left: 176px; top: 157px;
    font-size: 56px; font-weight: 800; line-height: 60px; color: var(--white);
    letter-spacing: -0.5px;
  }
  .hero-button {
    position: absolute; left: 176px; top: 317px; width: 228px; height: 36px;
    background: var(--band); color: var(--blue);
    font-size: 12px; font-weight: 500; line-height: 36px; text-align: center;
    text-decoration: none;
  }
  .categories { position: absolute; left: 0; top: 717px; width: 1200px; }
  .card {
    position: absolute; top: 0; width: 267px; height: 312px;
    background: var(--card-bg);
    box-shadow: 0 2px 6px rgba(0,0,0,0.12);
    padding: 28px 26px 0 26px;
  }
  .card h2 { font-size: 31px; font-weight: 500; line-height: 36px; color: var(--ink); height: 90px; }
  .card p { font-size: 11.5px; line-height: 16px; color: var(--ink-soft); margin-top: 8px; }
  .card .card-button {
    position: absolute; left: 26px; top: 246px; width: 140px; height: 36px;
    background: var(--blue); color: var(--white);
    font-size: 12px; font-weight: 600; line-height: 36px; text-align: center;
    text-decoration: none;
  }
  .to-top {
    position: absolute; left: 1089px; top: 1136px; width: 25px; height: 25px;
    background: var(--band);
    display: flex; align-items: center; justify-content: center;
  }
  .site-footer {
    position: absolute; left: 0; top: 1183px; width: 1200px; height: 65px;
    background: var(--band);
  }
</style>
</head>
<body>
  <div class="site">
    <header class="site-header">
      <div class="site-title"><strong style="font-weight:600">Das Echo</strong> der Wolken</div>
      <nav class="main-nav">
        <a href="#">HOME</a>
        <a href="#">BETRAGE</a>
        <a href="#">BUCH</a>
        <a href="#">KONTAKT</a>
        <a href="#">IMPRESSUM</a>
      </nav>
      <div class="search">Suche
        <svg width="13" height="13" viewBox="0 0 13 13"><circle cx="7.5" cy="5.5" r="4" fill="none" stroke="#2a3444" stroke-width="1.2"/><line x1="4.6" y1="8.4" x2="1" y2="12" stroke="#2a3444" stroke-width="1.3"/></svg>
      </div>
    </header>

    <div class="number-bar">
      <span class="label">und was sie erzählen:</span>
      <svg class="arrow" style="left:768px" width="6" height="8" viewBox="0 0 6 8"><path d="M6 0 L0 4 L6 8 Z" fill="#2a3444"/></svg>
      <div class="number-list">
        <a href="#" class="is-active">1</a><a href="#">2</a><a href="#">3</a><a href="#">4</a><a href="#">5</a><a href="#">6</a><a href="#">7</a><a href="#">8</a><a href="#">9</a>
      </div>
      <svg class="arrow" style="left:1017px" width="6" height="8" viewBox="0 0 6 8"><path d="M0 0 L6 4 L0 8 Z" fill="#1b7fe6"/></svg>
    </div>

    <section class="hero">
      <div class="hero-art" role="img" aria-label="Blaue Zahlenwolke mit Zahlen, Symbolen und nummerierten Dreiecken"></div>
      <h1 class="hero-title">Als die<br>Flüsse singen ...</h1>
      <a href="#" class="hero-button">Lern mehr</a>
    </section>

    <section class="categories">
      <article class="card" style="left:175px">
        <h2>Bibel und Zahlen</h2>
        <p>Die Heilige Schrift ist ein Werk aus Zahlen. Ihre Verfasser haben die archetypischen Inhalte in wundersamer Art und Weise in der Bibel. Und so weiter und so fort</p>
        <a href="#" class="card-button">Lern mehr</a>
      </article>
      <article class="card" style="left:466px">
        <h2>Naturwissens chaft</h2>
        <p>Die Heilige Schrift ist ein Werk aus Zahlen. Ihre Verfasser haben die archetypischen Inhalte in wundersamer Art</p>
        <a href="#" class="card-button">Lern mehr</a>
      </article>
      <article class="card" style="left:757px">
        <h2>Philosophie</h2>
        <p>Die Heilige Schrift ist ein Werk aus Zahlen. Ihre Verfasser haben die archetypischen Inhalte in wundersamer Art und Weise der Bibel. Und so weiter und so fort und vieles mehr das sehr schön eindrucksvoll ist</p>
        <a href="#" class="card-button">Lern mehr</a>
      </article>
    </section>

    <a href="#" class="to-top" aria-label="Nach oben">
      <svg width="12" height="10" viewBox="0 0 12 10"><path d="M6 0 L12 10 L0 10 Z" fill="#1f2530"/></svg>
    </a>

    <footer class="site-footer"></footer>
  </div>
</body>
</html>
```